Lumora Learning Web Design Project

Who We are:
Lumora Learning is education information portal/ magazine, providing information about the Chinese and International education markets. Our aim is to help school principals improve there curriculum, and parents in understanding this curriculum.

Project Brief:
The site will include education news updates, educational services, curriculum developments and overseas study. We hope the site represents the cross cultural bridge between the west and east. The site will cover both the Sciences and Arts.

Note:
The logo design competition is also underway so we only need the website design

What We want:
This competition is for Design only no coding!
Design a home page based on Template 1,2 or 3. I only need to select one.
The design of an article page.

Optional
Design a Microsoft Windows metro style splash page.

Sites We like:
http://www.kavelin.com.cn/kavelinlingo/default.aspx
http://www.brixtalacademia.co.uk/
http://qrpv.norvatestudio.net/

Template Explanations:
Template 1-
The main information has a dynamic sliding category view that when clicked displays the relevant info.
In addition to the main upper menu it also has a left hand sliding menu that pops out on click or gesture

Template 2-
Has limited number of Articles most of the menus are drop downs from the top menu

Template 3-
No Top menu

Target Market(s)

Teachers, principals and parents

Industry/Entity Type

Education

Requirements
Should not have
• kindergarten preschool feel

```html
<!DOCTYPE html>
<html lang="en">
<head>
<meta charset="utf-8">
<title>Lumora Learning</title>
<link href="https://fonts.googleapis.com/css2?family=Ubuntu:wght@400;500;700&family=Open+Sans:wght@400;600;700&display=swap" rel="stylesheet">
<style>
:root{
  --page:#e6e6e6;
  --white:#ffffff;
  --blue:#2f6fc0;
  --blue-dark:#1d4f98;
  --blue-light:#4a8ad6;
  --ink:#333333;
  --muted:#777777;
  --link:#3b5998;
  --bar:#333333;
  --leaf:#8bb33a;
  --yellow:#f4d23b;
  --line:#dddddd;
}
*{box-sizing:border-box;margin:0;padding:0}
html,body{width:1200px;height:1132px;overflow:hidden}
body{background:var(--page);font-family:"Open Sans",sans-serif;color:var(--ink);position:relative}
.abs{position:absolute}
.sheet{left:103px;top:15px;width:994px;height:980px;background:var(--white);box-shadow:0 0 3px rgba(0,0,0,.15)}
.header{left:103px;top:15px;width:994px;height:126px;background:linear-gradient(#fff,#f1f1f1)}
.brand{left:122px;top:60px;display:flex;align-items:center;gap:12px;font-family:"Ubuntu",sans-serif;font-size:36px;color:#444;font-weight:400}
.brand .dot{width:18px;height:18px;border-radius:50%;background:var(--blue)}
.search{left:915px;top:33px;width:168px;height:35px;border:1px solid #ccc;border-radius:18px;background:#fff;box-shadow:inset 0 1px 3px rgba(0,0,0,.1);font-family:"Ubuntu",sans-serif;font-size:15px;color:#777;padding:7px 14px}
.search svg{position:absolute;right:12px;top:7px}
.tab-end{width:14px;height:50px;background:var(--blue-dark);border-radius:10px 10px 0 0}
.nav{left:90px;top:141px;width:1020px;height:34px;background:linear-gradient(var(--blue-light),var(--blue));display:flex;padding-left:30px;font-family:"Ubuntu",sans-serif;font-size:14px;color:#fff}
.nav a{color:#fff;text-decoration:none;display:flex;align-items:center;justify-content:center;border-right:1px solid rgba(255,255,255,.25);height:34px}
.nav a.active{background:linear-gradient(#555,#222)}
.hero{left:116px;top:195px;width:646px;height:324px;background:linear-gradient(90deg,#4f6b6e,#8fb3b0 40%,#c9d6d0 70%,#8a8f86)}
.ribbon{left:90px;top:549px;width:225px;height:42px;background:linear-gradient(var(--blue-light),var(--blue-dark));border-radius:0 12px 12px 0;color:#fff;font-family:"Ubuntu",sans-serif;font-size:23px;padding:6px 0 0 41px}
.ribbon-fold{left:90px;top:535px;width:12px;height:20px;background:var(--blue-dark);border-radius:8px 8px 0 0}
.card{border:1px solid #e2e2e2;background:#fff;padding:10px}
.photo{width:289px;height:151px}
.list{list-style:none;font-size:11.5px;color:#444;letter-spacing:.2px}
.list li{height:24px;padding-left:16px;position:relative}
.list li::before{content:"";position:absolute;left:0;top:4px;border-left:4px solid var(--leaf);border-top:4px solid transparent;border-bottom:4px solid transparent}
.divider{left:445px;top:612px;height:342px;border-left:1px dotted #bbb}
.promo{left:787px;top:193px;width:300px;height:252px;border:1px solid #e2e2e2;background:#fff;padding:5px}
.promo-top{height:114px;background:linear-gradient(#1ea6dc,#0f7fc0);color:#fff;font-family:"Ubuntu",sans-serif;padding:4px 12px;line-height:1}
.promo-top .big{font-size:48px;font-weight:500}
.promo-top .small{font-size:26px}
.promo-top .yel{color:var(--yellow);font-size:32px;font-weight:500}
.promo-bot{margin-top:5px;height:118px;background:linear-gradient(90deg,#f3efe4,#d9d2bf);position:relative;font-family:"Ubuntu",sans-serif;color:#4a4637}
.promo-mark{position:absolute;left:10px;top:14px;width:40px;height:56px;background:#2a8fd6}
.promo-title{position:absolute;left:58px;top:12px;font-size:20px;line-height:21px;white-space:nowrap}
.promo-sub{position:absolute;left:58px;top:79px;font-size:13px;white-space:nowrap}
.promo-play{position:absolute;right:3px;bottom:2px}
.fb{left:793px;top:479px;width:292px;height:470px;border:1px solid #b8c0cc;background:#fff;font-size:11px}
.fb-head{height:24px;background:#edeff4;border-bottom:1px solid #d8dfea;font-weight:700;padding:4px 5px;color:#333}
.avatar{width:40px;height:40px;background:#d7d7d7}
.fb-name{color:var(--link);font-weight:700}
.fb-time{color:#888;font-size:9.5px}
.fb-post{font-size:10.5px;line-height:15px}
.scroll{left:276px;top:92px;width:13px;height:218px;background:#f0f0f0}
.faces{left:9px;top:337px;display:grid;grid-template-columns:repeat(6,42px);gap:3px}
.faces div{height:42px;background:linear-gradient(#b9a99a,#6f6a66)}
.side-tab{left:0;top:210px;width:56px;height:230px;background:linear-gradient(90deg,#1c5aa8,#4b8fd8);border-radius:0 8px 8px 0;border:1px solid #0f4a90}
.side-tab span{position:absolute;left:10px;top:180px;transform:rotate(-90deg);transform-origin:left top;color:#fff;font-family:"Ubuntu",sans-serif;font-size:30px;white-space:nowrap}
.share{left:0;top:500px;width:56px;height:232px;background:linear-gradient(90deg,#c8c8c8,#e9e9e9);border-radius:0 8px 8px 0;border:1px solid #b0b0b0}
.share .c{position:absolute;left:6px;width:39px;height:39px;border-radius:50%}
.footer{left:90px;top:994px;width:1020px;height:106px;background:linear-gradient(var(--blue-light),var(--blue))}
.foot-brand{left:122px;top:1038px;font-family:"Ubuntu",sans-serif;font-size:26px;color:#e8f0fb;display:flex;align-items:center;gap:10px}
.foot-brand .dot{width:14px;height:14px;border-radius:50%;background:#e8f0fb}
.flist{list-style:none;font-size:11px;color:#fff;letter-spacing:.3px}
.flist li{height:20px;padding-left:12px;position:relative;white-space:nowrap}
.flist li::before{content:"";position:absolute;left:0;top:6px;width:4px;height:4px;border-radius:50%;background:#fff}
.bottombar{left:90px;top:1100px;width:1020px;height:32px;background:var(--bar);color:#fff;font-size:10.5px;font-weight:600;display:flex;align-items:center;padding:0 10px 0 8px}
.bottombar a{color:#fff;text-decoration:none;padding:0 7px;border-right:1px solid #ccc;line-height:11px}
.bottombar a:last-of-type{border:none}
.bottombar .copy{margin-left:auto}
</style>
</head>
<body>
<div class="abs sheet"></div>
<header class="abs header"></header>
<div class="abs brand"><span>Lumora Learning</span><span class="dot"></span></div>
<div class="abs search">Search
  <svg width="22" height="20" viewBox="0 0 22 20"><circle cx="8" cy="8" r="6" fill="none" stroke="#aaa" stroke-width="1.6"/><line x1="12.5" y1="12.5" x2="19" y2="18" stroke="#aaa" stroke-width="2.4"/></svg>
</div>

<div class="abs tab-end" style="left:90px;top:125px"></div>
<div class="abs tab-end" style="left:1096px;top:125px"></div>
<nav class="abs nav">
  <a class="active" style="width:91px">Home</a>
  <a style="width:90px">News</a>
  <a style="width:111px">Comment</a>
  <a style="width:103px">Features</a>
  <a style="width:90px">Books</a>
  <a style="width:103px">Ranking</a>
  <a style="width:100px">Awards</a>
  <a style="width:80px">Jobs</a>
  <a style="width:114px">Subscribe</a>
  <a style="width:108px;border:none">Contact Us</a>
</nav>

<div class="abs hero" role="img" aria-label="Smiling student with glasses resting on books in a library, classmate behind"></div>

<div class="abs ribbon-fold"></div>
<div class="abs ribbon">Categories</div>

<div class="abs card" style="left:121px;top:607px;width:312px;height:172px">
  <div class="photo" role="img" aria-label="Classroom full of cheerful students" style="background:linear-gradient(#5b5a55,#8a7d70 60%,#b9a18a)"></div>
</div>
<div class="abs card" style="left:462px;top:606px;width:312px;height:172px">
  <div class="photo" role="img" aria-label="Young woman smiling over books in a library" style="background:linear-gradient(90deg,#3f8a95,#d9cfc6 45%,#6aa8ad)"></div>
</div>
<div class="abs divider"></div>

<ul class="abs list" style="left:121px;top:802px">
  <li>Removals, Relocation Local and Country Removals</li>
  <li>Office Relocation Interstate Removals</li>
  <li>Removals NSW Office Relocations</li>
  <li>Furniture Removals Sydney Prepack and Unpack</li>
  <li>Removals Storage - Long or Short Term</li>
  <li>Relocation Comprehensive range of boxes</li>
</ul>
<ul class="abs list" style="left:469px;top:804px">
  <li>Removals, Relocation Local and Country Removals</li>
  <li>Office Relocation Interstate Removals</li>
  <li>Removals NSW Office Relocations</li>
  <li>Furniture Removals Sydney Prepack and Unpack</li>
  <li>Removals Storage - Long or Short Term</li>
  <li>Relocation Comprehensive range of boxes</li>
</ul>

<aside class="abs promo">
  <div class="promo-top">
    <div><span class="big">Explore</span> <span class="small">your</span></div>
    <div class="yel">higher education</div>
    <div class="small" style="padding-left:55px">options on</div>
  </div>
  <div class="promo-bot">
    <div class="promo-mark"></div>
    <div class="promo-title">The Colleges<br>and Universities<br>of the Northvale Guild</div>
    <div class="promo-sub">(Heritage Circle) web site</div>
    <svg class="promo-play" width="34" height="34" viewBox="0 0 34 34"><rect x="1" y="1" width="32" height="32" rx="4" fill="#1a9ad8" stroke="#fff" stroke-width="2"/><path d="M13 9 L24 17 L13 25Z" fill="#fff"/></svg>
  </div>
</aside>

<aside class="abs fb">
  <div class="fb-head">Find us on Friendwall</div>
  <div class="abs avatar" style="left:10px;top:32px"></div>
  <div class="abs" style="left:54px;top:34px"><div class="fb-name">Dara Welling</div>
    <div style="margin-top:4px;font-size:9px">
      <span style="border:1px solid #ccc;background:#f3f3f3;color:#999;padding:1px 5px">&#10003; Like</span>&nbsp; You like this.</div></div>
  <div class="abs" style="left:0;top:82px;width:290px;border-top:1px solid #ddd"></div>
  <div class="abs avatar" style="left:10px;top:92px"></div>
  <div class="abs fb-post" style="left:58px;top:92px;width:190px">
    <div class="fb-name">Dara Welling</div>
    I think all of Mexico should throw a party for my birthday this year. Does May 5th work for you?
    <div class="fb-time" style="margin-top:3px">18 hours ago</div>
  </div>
  <div class="abs avatar" style="left:10px;top:182px"></div>
  <div class="abs fb-post" style="left:58px;top:182px;width:200px">
    <div class="fb-name">Dara Welling</div>
    Chirpline wants to give you $50 in advertising credit for FREE. Such a deal! <span style="color:var(--link)">https://chirpline.co/<br>DaraWelling</span>
    <div class="fb-time" style="margin-top:3px">Thursday at 17:46 near Larkfield, CO</div>
  </div>
  <div class="abs scroll"></div>
  <div class="abs" style="left:0;top:312px;width:290px;border-top:1px solid #ddd"></div>
  <div class="abs" style="left:8px;top:318px;font-size:9px">You and 14,596 others like <span style="color:var(--link)">Dara Welling</span>.</div>
  <div class="abs faces" role="img" aria-label="Profile pictures of page fans">
    <div></div><div></div><div></div><div></div><div></div><div></div>
    <div></div><div></div><div></div><div></div>
  </div>
  <div class="abs" style="left:0;top:431px;width:290px;border-top:1px solid #ddd"></div>
  <div class="abs" style="left:9px;top:437px;font-size:8.5px;color:#666;display:flex;gap:5px;align-items:center"><span style="width:10px;height:10px;background:var(--link);display:inline-block"></span>Friendwall social plugin</div>
</aside>

<div class="abs side-tab"><span>Tab Menu</span></div>
<div class="abs share">
  <div class="c" style="top:25px;background:#1e4f8f"></div>
  <div class="c" style="top:75px;background:#2aa6e0"></div>
  <div class="c" style="top:125px;background:#f29318"></div>
  <div class="c" style="top:175px;background:#555">
    <svg width="39" height="39" viewBox="0 0 39 39"><rect x="12" y="14" width="15" height="11" fill="none" stroke="#fff" stroke-width="1.5"/><path d="M12 14 L19.5 20 L27 14" fill="none" stroke="#fff" stroke-width="1.5"/></svg>
  </div>
</div>

<div class="abs tab-end" style="left:90px;top:978px;height:30px"></div>
<div class="abs tab-end" style="left:1096px;top:978px;height:30px"></div>
<footer class="abs footer"></footer>
<div class="abs foot-brand"><span>Lumora Learning</span><span class="dot"></span></div>
<ul class="abs flist" style="left:381px;top:1010px">
  <li>Tavi's Fresh Food Essentials</li><li>Tavi's Fresh Food Desserts</li><li>Tavi's Fresh Food Kitchen</li><li>Tavi's Ready Mixes</li>
</ul>
<ul class="abs flist" style="left:571px;top:1011px">
  <li>About</li><li>Services</li><li>Wellness Education</li><li>Schedule a Consult</li>
</ul>
<ul class="abs flist" style="left:732px;top:1011px">
  <li>Tavi's Fresh Food Essentials</li><li>Tavi's Fresh Food Desserts</li><li>Tavi's Fresh Food Kitchen</li><li>Tavi's Ready Mixes</li>
</ul>
<ul class="abs flist" style="left:932px;top:1014px">
  <li>Tavi's Fresh Food Essentials</li><li>Tavi's Fresh Food Desserts</li><li>Tavi's Fresh Food Kitchen</li><li>Tavi's Ready Mixes</li>
</ul>
<div class="abs bottombar">
  <a>Home</a><a>News</a><a>Comment</a><a>Features</a><a>Books</a><a>Ranking</a><a>Awards</a><a>Jobs</a><a>Subscribe</a><a>Contact Us</a>
  <span class="copy">(c) Copyright All Right Recieved</span>
</div>
</body>
</html>
```